Fizz Bop Lantern Series 1 Volume 1

I am looking for someone to make me a book cover, I want something catchy but classy.

The title of the book is; Fizz Bop Lantern
Series 1 Volume 1

Colors should be: Red, White, Black and Grey

```html
<!DOCTYPE html>
<html lang="en">
<head>
<meta charset="utf-8">
<title>Fizz Bop Lantern – Series 1 Volume 1</title>
<link rel="stylesheet" href="https://fonts.googleapis.com/css2?family=Montserrat:wght@500;600;700&display=swap">
<style>
  :root {
    --backdrop: #8f8f8f;
    --paper: #ffffff;
    --title-grey: #4a4a4a;
    --subtitle-grey: #6a6a6a;
    --accent-red: #c8202a;
    --ink-black: #1c1c1c;
    --soft-grey: #d9d9d9;
  }
  * { margin: 0; padding: 0; box-sizing: border-box; }
  html, body {
    width: 1200px;
    height: 1101px;
    overflow: hidden;
    background: var(--backdrop);
  }
  .canvas {
    position: relative;
    width: 1200px;
    height: 1101px;
  }
  .book-cover {
    position: absolute;
    left: 310px;
    top: 50px;
    width: 580px;
    height: 1000px;
    background: var(--paper);
    font-family: "Montserrat", sans-serif;
    overflow: hidden;
  }
  .title-block {
    position: absolute;
    top: 105px;
    left: 0;
    width: 100%;
    text-align: center;
  }
  .title-line {
    display: block;
    color: var(--title-grey);
    font-weight: 700;
    font-size: 52px;
    line-height: 74px;
    letter-spacing: 14px;
    text-transform: uppercase;
  }
  .title-line--first {
    display: flex;
    justify-content: center;
    align-items: center;
    gap: 14px;
  }
  .title-mark {
    width: 34px;
    height: 38px;
    background: var(--title-grey);
  }
  .series-label {
    margin-top: 26px;
    color: var(--subtitle-grey);
    font-weight: 600;
    font-size: 15px;
    letter-spacing: 8px;
    text-transform: uppercase;
  }
  .cover-photo {
    position: absolute;
    top: 372px;
    left: 0;
    width: 400px;
    height: 490px;
    background: linear-gradient(100deg, var(--ink-black) 0%, #3a3a3a 40%, var(--soft-grey) 55%, var(--accent-red) 75%, var(--paper) 100%);
  }
  .author-name {
    position: absolute;
    bottom: 48px;
    left: 0;
    width: 100%;
    text-align: center;
    color: var(--accent-red);
    font-weight: 700;
    font-size: 20px;
    letter-spacing: 4px;
  }
</style>
</head>
<body>
  <main class="canvas">
    <section class="book-cover">
      <header class="title-block">
        <h1>
          <span class="title-line title-line--first"><span class="title-mark" aria-hidden="true"></span>Fizz</span>
          <span class="title-line">Bop</span>
          <span class="title-line">Lantern</span>
        </h1>
        <p class="series-label">Series 1 Volume 1</p>
      </header>
      <div class="cover-photo" role="img" aria-label="Photo of black and white office binders on shelves with a hand in a white sleeve pulling out a red binder"></div>
      <p class="author-name">Marla Jean Tuckett</p>
    </section>
  </main>
</body>
</html>
```